Web Design for Financial Consulting Company

We need a website design for a financial consulting company "Kelvane Consulting". We build financial models, scenario analysis, handle the budgeting process and provide temporary staffing. I have over 10 years of experience. My Excel expertise and analytical savvy has saved clients over $17 million in profit.

Target Market(s)

Small to medium businesses

Industry/Entity Type

Financial Consulting

Number of Pages Required

4 page

Requirements
Must have
• Professional looking
Nice to have
• A little futuristic looking

```html
<!DOCTYPE html>
<html lang="en">
<head>
<meta charset="utf-8">
<title>Kelvane Consulting</title>
<link rel="stylesheet" href="https://fonts.googleapis.com/css2?family=Poppins:wght@400;500;600;700;800&display=swap">
<style>
:root{
  --navy:#0f4a73;
  --navy-deep:#0d3f63;
  --bright:#0aa6ef;
  --ink:#1d2b36;
  --text:#3d4750;
  --muted:#e7e9ec;
  --footer:#172633;
  --white:#fff;
}
*{box-sizing:border-box;margin:0;padding:0}
html,body{width:1200px;height:3688px;overflow:hidden}
body{position:relative;background:var(--white);font-family:"Poppins",sans-serif;color:var(--ink)}
.abs{position:absolute}
.btn{position:absolute;background:var(--bright);color:#fff;font-weight:700;font-size:14px;display:flex;align-items:center;justify-content:center;text-transform:uppercase}

/* header */
.brand{position:absolute;font-weight:700;font-size:26px;line-height:1;color:var(--navy);white-space:nowrap}
.nav{position:absolute;top:28px;left:616px;display:flex;gap:28px;font-size:14px;font-weight:600}
.nav a{color:var(--ink);text-decoration:none}
.nav a.active{color:var(--bright);position:relative}
.nav a.active::before{content:"";position:absolute;left:0;right:0;top:-28px;height:3px;background:var(--bright)}

/* hero */
.hero-kicker{left:90px;top:276px;font-weight:700;font-size:20px;color:#fff;display:flex;align-items:center;gap:10px}
.hero-kicker::before{content:"";width:52px;height:2px;background:#fff}
.hero-title{left:86px;top:302px;font-weight:800;font-size:47px;line-height:56px;color:#fff}
.hero-text{left:90px;top:428px;width:460px;font-size:18px;line-height:24px;color:#fff}

/* headings */
.section-title{position:absolute;left:0;width:1200px;text-align:center;font-weight:800;color:var(--navy);font-size:40px;line-height:48px}
.rule{position:absolute;height:2px;width:60px;background:var(--bright)}

/* about */
.kicker{font-weight:700;font-size:15px;color:var(--bright);display:flex;align-items:center;gap:10px}
.kicker::before{content:"";width:36px;height:2px;background:var(--bright)}
.about-title{left:660px;top:918px;font-weight:800;font-size:40px;color:var(--navy)}
.about-text{left:660px;top:975px;width:350px;font-size:15px;line-height:22px;color:var(--text)}

/* stats */
.stat{position:absolute;top:1476px;width:135px;height:135px;background:#fff;box-shadow:0 10px 30px rgba(0,0,0,.08);text-align:center;padding-top:34px}
.stat b{display:block;font-size:34px;font-weight:700;color:var(--bright);line-height:1}
.stat span{display:block;font-size:12px;font-weight:600;margin-top:14px}

/* services */
.card{position:absolute;top:1794px;width:245px;height:361px;background:#fff;box-shadow:0 8px 24px rgba(0,0,0,.07)}
.card .photo{height:198px}
.card h3{margin:32px 18px 0;font-size:17px;line-height:22px;font-weight:800;color:var(--navy)}
.card p{margin:12px 18px 0;font-size:13px;line-height:17px;color:var(--text)}
.card .go{position:absolute;bottom:-22px;right:28px;width:36px;height:36px;background:var(--navy);display:flex;align-items:center;justify-content:center}
.card .go.alt{background:var(--bright)}

/* contact */
.info{position:absolute;left:197px;display:flex;gap:15px;align-items:center}
.info .ico{width:66px;height:66px;display:flex;align-items:center;justify-content:center;background:var(--bright)}
.info .ico.dark{background:var(--navy)}
.info h4{font-size:22px;font-weight:800;color:var(--navy);line-height:24px}
.info p{font-size:20px;color:var(--ink);line-height:24px}
.label{position:absolute;font-size:11px;font-weight:700}
.field{position:absolute;background:var(--muted);font-size:12px;color:#8a939b;padding:14px 15px}

/* footer */
.foot-h{position:absolute;top:3365px;font-weight:700;font-size:17px;color:#fff}
.foot-list{position:absolute;font-size:13px;color:#fff;line-height:31px}
.foot-item{position:absolute;left:656px;font-size:13px;color:#fff;line-height:17px;padding-left:22px}
.soc{position:absolute;top:3419px;width:29px;height:29px;border-radius:50%;background:#2a3a47;border:1px solid #3f5060}
</style>
</head>
<body>

<!-- header -->
<div class="brand" style="left:88px;top:24px">Kelvane Consulting</div>
<nav class="nav">
  <a class="active">HOME</a><a>ABOUT US</a><a>SERVICES</a><a>CONTACT US</a>
</nav>
<div class="btn" style="left:1001px;top:20px;width:110px;height:34px;font-size:13px">RIGISTER</div>

<!-- hero -->
<svg class="abs" style="left:0;top:75px" width="1200" height="595">
  <rect width="1200" height="595" fill="var(--navy)"/>
  <polygon points="740,0 1200,0 1200,595 456,595" fill="#fff"/>
  <polygon points="760,0 1200,0 1200,595 476,595" fill="#b8bec4" role="img" aria-label="Photo of two finance consultants reviewing a document together"/>
</svg>
<div class="abs hero-kicker">WE HELPING YOUR</div>
<h1 class="abs hero-title">FINANCE TEAM &amp;<br>INCREASING PROFIT</h1>
<p class="abs hero-text">Great for renovations, construction, roofing, clean fill, concrete, estate clean-outs.</p>
<div class="btn" style="left:90px;top:539px;width:135px;height:43px">GET STARTED</div>

<!-- about -->
<svg class="abs" style="left:160px;top:770px" width="450" height="500">
  <polygon points="70,8 432,8 373,480 12,482" fill="#8a939a" role="img" aria-label="Photo of a consulting team working at a laptop"/>
</svg>
<div class="abs kicker" style="left:660px;top:897px">ABOUT US</div>
<h2 class="abs about-title">KELVANE</h2>
<p class="abs about-text">I am an experienced Finance professional who develops strategic financial plans, provides insightful analysis, and supports decision-making. With over 10 years of experience, I have successfully increased profitability for clients by $17M.</p>
<div class="btn" style="left:660px;top:1127px;width:135px;height:43px">GET STARTED</div>

<!-- stats -->
<h2 class="section-title" style="top:1343px">OUR WORK IMPRESSIONS<br>GOING HIGH</h2>
<div class="rule" style="left:570px;top:1451px"></div>
<div class="stat" style="left:290px"><b>300+</b><span>ANALYSIS</span></div>
<div class="stat" style="left:452px"><b>120+</b><span>GET REWARDS</span></div>
<div class="stat" style="left:613px"><b>921+</b><span>CLIENTS</span></div>
<div class="stat" style="left:775px"><b>100+</b><span>PROFIT</span></div>

<!-- services -->
<svg class="abs" style="left:0;top:1670px" width="1200" height="595">
  <polygon points="893,0 1200,0 1200,594 610,594" fill="var(--bright)"/>
</svg>
<h2 class="section-title" style="top:1716px">OUR SERVICES</h2>
<div class="rule" style="left:567px;top:1768px"></div>

<div class="card" style="left:89px">
  <div class="photo" style="background:#8f9aa3" role="img" aria-label="Photo of consultants discussing financial models"></div>
  <h3>FINANCIAL MODELS<br>– PROJECTS</h3>
  <p>Financial analysis, scenario modeling, pricing analysis, projects</p>
  <div class="go"><svg width="12" height="12" viewBox="0 0 12 12"><path d="M4 2l4 4-4 4" stroke="#fff" stroke-width="2" fill="none"/></svg></div>
</div>
<div class="card" style="left:347px">
  <div class="photo" style="background:#a08a6f" role="img" aria-label="Photo of a desk with budget papers and a calculator"></div>
  <h3>BUDGETING<br>PROCESS</h3>
  <p>Building budgets from scratch, revamping current process to be more robust and scalable.</p>
  <div class="go alt"><svg width="12" height="12" viewBox="0 0 12 12"><path d="M4 2l4 4-4 4" stroke="#fff" stroke-width="2" fill="none"/></svg></div>
</div>
<div class="card" style="left:604px">
  <div class="photo" style="background:#7a6a63" role="img" aria-label="Photo of temporary staff reviewing paperwork"></div>
  <h3>TEMPORARY<br>STAFFING</h3>
  <p>Years of Financial Planning &amp; Analysis experience across multiple industries can help..</p>
  <div class="go"><svg width="12" height="12" viewBox="0 0 12 12"><path d="M4 2l4 4-4 4" stroke="#fff" stroke-width="2" fill="none"/></svg></div>
</div>
<div class="card" style="left:861px">
  <div class="photo" style="background:#b3b0a8" role="img" aria-label="Photo of a team meeting about process improvement"></div>
  <h3>PROCESS<br>IMPROVEMENT</h3>
  <p>Month end close, reporting, budgeting</p>
  <div class="go"><svg width="12" height="12" viewBox="0 0 12 12"><path d="M4 2l4 4-4 4" stroke="#fff" stroke-width="2" fill="none"/></svg></div>
</div>

<!-- contact -->
<h2 class="section-title" style="top:2336px">GET IN TOUCH</h2>
<div class="rule" style="left:570px;top:2391px"></div>
<p class="abs" style="left:0;width:1200px;text-align:center;top:2418px;font-size:14px">Please fill out the information below to complete...</p>

<div class="info" style="top:2501px">
  <div class="ico"><svg width="28" height="28" viewBox="0 0 24 24"><path d="M6.6 10.8a15 15 0 006.6 6.6l2.2-2.2a1 1 0 011-.25 11.4 11.4 0 003.6.57 1 1 0 011 1V20a1 1 0 01-1 1A17 17 0 013 4a1 1 0 011-1h3.5a1 1 0 011 1c0 1.25.2 2.45.57 3.57a1 1 0 01-.25 1z" fill="#fff"/></svg></div>
  <div><h4>PHONE:</h4><p>123 4567 655</p></div>
</div>
<div class="info" style="top:2593px">
  <div class="ico dark"><svg width="26" height="20" viewBox="0 0 26 20"><rect x="1" y="1" width="24" height="18" fill="#fff"/><path d="M1 2l12 9 12-9" stroke="var(--navy)" stroke-width="2" fill="none"/></svg></div>
  <div><h4>EMAIL:</h4><p>info@example.com</p></div>
</div>
<div class="info" style="top:2685px">
  <div class="ico"><svg width="22" height="30" viewBox="0 0 22 30"><path d="M11 0a11 11 0 0111 11c0 8-11 19-11 19S0 19 0 11A11 11 0 0111 0z" fill="#fff"/><circle cx="11" cy="11" r="4" fill="var(--bright)"/></svg></div>
  <div><h4>LCATIONSS:</h4><p>Some goes address here</p></div>
</div>

<div class="label" style="left:599px;top:2499px">NAME*</div>
<div class="label" style="left:806px;top:2499px">EMAIL*</div>
<div class="field" style="left:602px;top:2518px;width:198px;height:39px">Enter your name</div>
<div class="field" style="left:808px;top:2518px;width:197px;height:39px">Enter your email</div>
<div class="label" style="left:599px;top:2568px">PHONE*</div>
<div class="label" style="left:806px;top:2568px">COMPANY</div>
<div class="field" style="left:602px;top:2587px;width:198px;height:39px">Enter phone number</div>
<div class="field" style="left:808px;top:2587px;width:197px;height:39px;display:flex;justify-content:space-between">Select company<svg width="10" height="10" viewBox="0 0 10 10" style="margin-top:3px"><path d="M2 3l3 3 3-3" stroke="#444" stroke-width="1.5" fill="none"/></svg></div>
<div class="label" style="left:599px;top:2642px">PHONE*</div>
<div class="field" style="left:602px;top:2662px;width:403px;height:111px">Type your text...</div>
<div class="btn" style="left:601px;top:2801px;width:404px;height:48px;font-size:15px">SUBMIT NOW
  <svg style="position:absolute;right:22px" width="20" height="18" viewBox="0 0 20 18"><path d="M1 8L19 1l-4 16-5-6z" fill="#fff"/></svg>
</div>

<!-- footer -->
<svg class="abs" style="left:0;top:2960px" width="1200" height="728">
  <polygon points="0,10 1200,340 1200,728 0,728" fill="var(--footer)"/>
</svg>
<div class="abs" style="left:212px;top:2925px;width:776px;height:333px;background:linear-gradient(135deg,#c4d3de,#aabfcd)" role="img" aria-label="Map showing the office location with a pin"></div>

<div class="brand" style="left:150px;top:3432px;color:#fff;font-size:22px">Kelvane Consulting</div>

<div class="foot-h" style="left:423px">QUICK LINKS</div>
<div class="foot-list" style="left:423px;top:3410px">› &nbsp;Home<br>› &nbsp;About Us<br>› &nbsp;Services<br>› &nbsp;Contact Us</div>

<div class="foot-h" style="left:656px">CONTACT INFO</div>
<div class="foot-item" style="top:3414px">Email:<br>info@example.com</div>
<div class="foot-item" style="top:3471px">Phone:<br>0123.456.789</div>
<div class="foot-item" style="top:3525px">Location:<br>some address gose here</div>
<svg class="abs" style="left:656px;top:3417px" width="16" height="140">
  <rect x="1" y="2" width="13" height="9" fill="var(--bright)"/>
  <circle cx="7" cy="61" r="5" fill="var(--bright)"/>
  <path d="M7 109a5 5 0 015 5c0 4-5 9-5 9s-5-5-5-9a5 5 0 015-5z" fill="var(--bright)"/>
</svg>

<div class="foot-h" style="left:911px">FOLLOW US</div>
<div class="soc" style="left:913px"></div>
<div class="soc" style="left:949px"></div>
<div class="soc" style="left:984px"></div>
<div class="soc" style="left:1020px"></div>

<p class="abs" style="left:0;width:1200px;text-align:center;top:3647px;font-size:13px;font-weight:600;color:#fff">© 2023, Kelvane Consulting | All rights reserved</p>
<div class="abs" style="left:1133px;top:3603px;width:40px;height:40px;border-radius:50%;background:var(--bright);display:flex;align-items:center;justify-content:center">
  <svg width="12" height="12" viewBox="0 0 12 12"><path d="M2 8l4-4 4 4" stroke="#fff" stroke-width="1.6" fill="none"/></svg>
</div>

</body>
</html>
```